Tarrendale Secondary College House displays

Our school has 4 new houses that are designed to promote school connectedness and school pride. Each house display should include the name of the house, a silhouette portrait of the person the house is named after and a famous quote from that person. Each house display should also promote the unique house colour. Details are included in the attached word document. I have also attached a Marcus Threlby poster that gives some sort of idea about the look and feel we are after. The house name should be quite prominent.

Target Market(s)

Tarrendale Secondary College has 1800 students. We are a unique school committed to a strengths based program. Our house system is designed to connect students to each other and to the school. To understand our school visit our website at www.tarrendalesc.vic.edu.au

Logo Text

We want a logo for each of our houses that has the house name on it - see the attached word document for details.

Font styles to use
Sans Serif

Colors
0792cd
00a990
fbed22
ec1f27

Requirements
Must have
• Colour- each house must include the colour it is aligned to. This is outlined in the attached word document

```html
<!DOCTYPE html>
<html lang="en">
<head>
<meta charset="utf-8">
<title>Tarrendale Secondary College House displays</title>
<link rel="stylesheet" href="https://fonts.googleapis.com/css2?family=Montserrat:wght@800;900&display=swap">
<style>
  :root {
    --page-bg: #f2f2f2;
    --gold-light: #fbed22;
    --gold-mid: #ffcc00;
    --gold-deep: #f7a400;
    --gold-ink: #141008;
    --blue-deep: #0a2c8c;
    --blue-mid: #1356c4;
    --blue-light: #0792cd;
    --teal-light: #2bb3c9;
    --white: #ffffff;
    --display-font: "Montserrat", "Arial Black", sans-serif;
  }
  * { margin: 0; padding: 0; box-sizing: border-box; }
  html, body {
    width: 1200px;
    height: 848px;
    overflow: hidden;
    background: var(--page-bg);
  }
  .canvas {
    position: relative;
    width: 1200px;
    height: 848px;
  }
  .house-poster {
    position: absolute;
    top: 262px;
    width: 547px;
    height: 385px;
    overflow: hidden;
    box-shadow: 2px 3px 6px rgba(0, 0, 0, 0.45);
  }
  .house-poster--gold {
    left: 35px;
    background: linear-gradient(160deg, var(--gold-deep) 0%, var(--gold-mid) 45%, var(--gold-light) 100%);
  }
  .house-poster--blue {
    left: 619px;
    background: linear-gradient(120deg, var(--blue-deep) 0%, var(--blue-mid) 45%, var(--blue-light) 75%, var(--teal-light) 100%);
  }
  .portrait-area {
    position: absolute;
    top: 0;
    bottom: 0;
  }
  .house-poster--gold .portrait-area {
    left: 285px;
    right: 0;
    background: radial-gradient(ellipse at 55% 40%, rgba(60, 40, 0, 0.55) 0%, rgba(120, 90, 0, 0.35) 45%, rgba(251, 237, 34, 0) 75%);
  }
  .house-poster--blue .portrait-area--left {
    left: 0;
    width: 250px;
    background: radial-gradient(ellipse at 50% 55%, rgba(5, 15, 60, 0.75) 0%, rgba(10, 40, 120, 0.4) 55%, rgba(10, 44, 140, 0) 85%);
  }
  .house-poster--blue .portrait-area--right {
    left: 270px;
    right: 0;
    background: radial-gradient(ellipse at 65% 40%, rgba(120, 220, 230, 0.45) 0%, rgba(43, 179, 201, 0.25) 50%, rgba(7, 146, 205, 0) 85%);
  }
  .house-name {
    position: absolute;
    font-family: var(--display-font);
    font-weight: 900;
    text-transform: uppercase;
    letter-spacing: 1px;
    line-height: 1;
  }
  .house-poster--gold .house-name {
    left: 22px;
    top: 26px;
    font-size: 40px;
    color: var(--gold-ink);
  }
  .house-poster--blue .house-name {
    right: 22px;
    bottom: 22px;
    font-size: 34px;
    color: var(--white);
  }
  .house-quote {
    position: absolute;
    font-family: var(--display-font);
    font-weight: 800;
    font-variant: small-caps;
    text-align: center;
    letter-spacing: 0.5px;
  }
  .house-poster--gold .house-quote {
    left: 0;
    width: 312px;
    top: 130px;
    font-size: 23px;
    line-height: 24.5px;
    color: var(--gold-ink);
  }
  .house-poster--blue .house-quote {
    left: 135px;
    width: 400px;
    top: 122px;
    font-size: 19px;
    line-height: 21px;
    color: var(--white);
  }
</style>
</head>
<body>
<main class="canvas">
  <section class="house-poster house-poster--gold">
    <div class="portrait-area" role="img" aria-label="Toned portrait photograph of the house namesake in yellow and orange"></div>
    <h2 class="house-name">Waratah</h2>
    <p class="house-quote">"I laid in bed<br>thinking about<br>the future.<br>How I would like it<br>to be,<br>even if<br>I am not there."</p>
  </section>
  <section class="house-poster house-poster--blue">
    <div class="portrait-area portrait-area--left" role="img" aria-label="Toned photograph of the house namesake playing football in blue"></div>
    <div class="portrait-area portrait-area--right" role="img" aria-label="Toned close-up portrait photograph of the house namesake smiling in blue"></div>
    <p class="house-quote">"I love life.<br>There's always something<br>to overcome,<br>new people to meet...<br>You've just got<br>to find your bliss<br>and go after it.<br>That's where the drive is,<br>that's how you find<br>your special place."</p>
    <h2 class="house-name">Banksia</h2>
  </section>
</main>
</body>
</html>
```